Professional & attention grabbing.

A business card design, front and back. I already have a logo I will attach, but I am open to something new as well.
Things to include:
Name:
Title:
Phone:
Email:
Wanting something that is professional but attention grabbing.
Also we do a lot of work using drones on natural gas pipelines (leading the future)if you want to include any of that. I'm open to ideas.
Target Market(s)
Natural gas transmission industry / greenhouse gas mitigation industry
Industry/Entity Type
Business
Contact Information for Business Card
All details have been conveyed above.
Colors
Designer to choose colors to be used in the design.
Look and feel
Each slider illustrates characteristics of the customer's brand and the style your logo design should communicate.

```html
<!DOCTYPE html>
<html lang="en">
<head>
<meta charset="utf-8">
<title>Kestrel Vale Inspections – Business Card</title>
<link rel="stylesheet" href="https://fonts.googleapis.com/css2?family=Roboto:wght@400;500;700;900&display=swap">
<style>
  :root {
    --bg: #5a5a5c;
    --card-top: #38383b;
    --card-bottom: #1d1d1f;
    --red: #e0231c;
    --white: #ffffff;
    --soft: #d8d8d8;
    --rule: #9a9a9a;
  }
  * { box-sizing: border-box; margin: 0; padding: 0; }
  html, body { width: 1200px; height: 852px; overflow: hidden; }
  body {
    background: var(--bg);
    font-family: "Roboto", Arial, sans-serif;
    position: relative;
  }
  .card {
    position: absolute;
    width: 560px;
    height: 320px;
    border-radius: 18px;
    background: linear-gradient(160deg, var(--card-top), var(--card-bottom));
    overflow: hidden;
    box-shadow: 0 10px 24px rgba(0,0,0,.35);
  }
  .card--front { left: 60px; top: 90px; }
  .card--back { left: 580px; top: 442px; }

  /* Front */
  .front__band-top {
    position: absolute;
    right: 0; top: 96px;
    width: 250px; height: 16px;
    background: var(--red);
  }
  .brand {
    display: flex;
    align-items: center;
    gap: 10px;
  }
  .brand__mark {
    width: 26px; height: 26px;
    background: var(--red);
    flex: none;
  }
  .brand__name {
    color: var(--white);
    font-weight: 700;
    font-size: 24px;
    line-height: 1.05;
    letter-spacing: .5px;
    text-transform: uppercase;
  }
  .card--front .brand {
    position: absolute;
    left: 130px; top: 124px;
  }
  .front__tagline {
    position: absolute;
    left: 0; right: 0; bottom: 34px;
    height: 34px;
    background: var(--red);
    color: var(--white);
    font-size: 15px;
    font-weight: 500;
    display: flex;
    align-items: center;
    justify-content: center;
  }

  /* Back */
  .card--back .brand {
    position: absolute;
    left: 40px; top: 140px;
    width: 230px;
  }
  .card--back .brand__name { font-size: 20px; }
  .back__divider {
    position: absolute;
    left: 292px; top: 60px;
    width: 1px; height: 190px;
    background: var(--rule);
  }
  .contact {
    position: absolute;
    left: 312px; top: 78px;
  }
  .contact__name {
    color: var(--red);
    font-weight: 700;
    font-size: 20px;
    letter-spacing: 1px;
    text-transform: uppercase;
  }
  .contact__title {
    color: var(--soft);
    font-size: 12.5px;
    margin-top: 2px;
    margin-bottom: 14px;
  }
  .contact__list { list-style: none; }
  .contact__item {
    display: flex;
    align-items: center;
    gap: 9px;
    color: var(--soft);
    font-size: 12.5px;
    margin-bottom: 7px;
  }
  .contact__icon { width: 12px; height: 12px; flex: none; }
</style>
</head>
<body>

<section class="card card--front" aria-label="Card front">
  <div class="front__band-top"></div>
  <div class="brand">
    <span class="brand__mark"></span>
    <span class="brand__name">Kestrel Vale<br>Inspections</span>
  </div>
  <p class="front__tagline">Also we do a lot of work using drones on natural gas pipelines</p>
</section>

<section class="card card--back" aria-label="Card back">
  <div class="brand">
    <span class="brand__mark"></span>
    <span class="brand__name">Kestrel Vale<br>Inspections</span>
  </div>
  <div class="back__divider"></div>
  <div class="contact">
    <h1 class="contact__name">Daniel Reed</h1>
    <p class="contact__title">Managing Director</p>
    <ul class="contact__list">
      <li class="contact__item">
        <svg class="contact__icon" viewBox="0 0 12 12"><path fill="#e0231c" d="M2.5 1l2 2.2-1 1.3a7 7 0 0 0 4 4l1.3-1L11 9.5 9.6 11C5 11 1 7 1 2.4z"/></svg>
        1300 555 014
      </li>
      <li class="contact__item">
        <svg class="contact__icon" viewBox="0 0 12 12"><circle cx="6" cy="6" r="5" fill="none" stroke="#e0231c" stroke-width="1.4"/><path d="M1 6h10M6 1c-2.5 3-2.5 7 0 10M6 1c2.5 3 2.5 7 0 10" fill="none" stroke="#e0231c" stroke-width="1"/></svg>
        www.kestrelvaledemo.com
      </li>
      <li class="contact__item">
        <svg class="contact__icon" viewBox="0 0 12 12"><rect x="0.5" y="2" width="11" height="8" fill="#e0231c"/><path d="M0.5 2.5L6 6.5l5.5-4" fill="none" stroke="#1d1d1f" stroke-width="1"/></svg>
        daniel.reed@kestrelvaledemo.com
      </li>
    </ul>
  </div>
</section>

</body>
</html>
```